Funky Modern Flyer A5 or Postcard size

Hi, I am looking at a one small flyer (A5 or postcard size) that I can put both on my website on the front page (ie so png) and also send out if necessary.

It has to be modern, funky and hip. My brand is professional / Corporate so it also has to fit in with that brand.

There are 6 attachments:
Example 1 - FernaPeak - I like this look, clean, modern, funky and says it all.
Example 2 - FernPeak - again another look I like, simple, explanatory
Example 4 - Brightstall Bazaar - font is cool on this one but background not so much too much going on but I like the font
Example 5 - Example 4 - Brightstall Bazaar - font is cool on this one but background not so much too much going on but I like the font
5 is my logo
Example 6 is something I found on the web this morning which is effective.

It is for a Mentoring and Training program I run called: HIGHSTRIDE

What is to be included is the following:
The name: Highstride
Somewhere: Training, Mentoring
My Logo (see attached two options) you can choose which colour suits and I have the source file should you need it
My website and email: www.miriambaskell.example / miriam@miriambaskell.example

This wording: This is one of our highest in-demand programs and is based on a background and proven track record by Miriam in accelerating sales organisations and their people into stand out high performers. **(NOTE this wording in this paragraph may change and I am open to you changing if you think you can make it more effective!)

Colours: white, black and gold (those are our website colours).

I'd like the Highstride to really stand out.... I have included two fonts that I really like that I got off Brightstall Bazaar. However, feel free to suggest other fonts that you think cool or funky!
Updates

Hi everyone, just to add a note to the brief, I am not overly keen on pictures that are really busy. I only like a picture that is minimal and effective. The examples from Brightstall Bazaar was more for the Font Style not so much the pictures in the background. The pictures can take away from a design unless done really minimally.....hope this makes sense. Miriam Added Wednesday, March 15, 2017

Target Market(s)

My target Market is Corporates but I want a Funky Modern look as a lot of people in Corporates are Millennials as well which is part of my target market

Industry/Entity Type

Information Technology

Requirements
Must have
• What is to be included is the following:
• The name: Highstride
• Somewhere: Training, Mentoring
• My Logo (see attached two options) you can choose which colour suits and I have the source file should you need it
• My website and email: www.miriambaskell.example / miriam@miriambaskell.example
• This wording: This is one of our highest in-demand programs and is based on a background and proven track record in high performance and accelerating sales organisations and their people into stand out high performers. (**NOTE this wording may change when final design is picked to be changed as still working in it***)
• Colours: white, black and gold (those are our website colours).
• I'd like the Highstride to really stand out.... I have included two fonts that I really like that I got off Brightstall Bazaar. However, feel free to suggest other fonts that you think cool or funky! NOTE: The pictures I have attached is mainly for the FONTS not for the background pictures. I am not that keen on background pictures as it can take away from the font - unless it is minimal
Should not have
• Too many different colours, I like slick, modern, clean. White, gold and black preferred as this is our website colour.
• NOTE: The pictures from Brightstall Bazaar I have attached are mainly for the FONTS not for the background pictures. I am not hugely keen on background pictures as it can take away from the font/message - unless the pictures are minimal but effective.

```html
<!DOCTYPE html>
<html lang="en">
<head>
<meta charset="utf-8">
<title>Highstride – Training, Mentoring Flyer</title>
<link rel="stylesheet" href="https://fonts.googleapis.com/css2?family=Montserrat:wght@300;400&family=Figtree:wght@400&family=Permanent+Marker&display=swap">
<style>
  :root {
    --page: #ffffff;
    --gold: #d8b14c;
    --ink: #333333;
    --brand-grey: #555555;
    --photo-light: #ececec;
    --photo-mid: #f7f7f7;
    --photo-dark: #1f1f1f;
  }
  * { margin: 0; padding: 0; box-sizing: border-box; }
  html, body {
    width: 1200px;
    height: 1200px;
    overflow: hidden;
    background: var(--page);
  }
  .flyer {
    position: absolute;
    left: 40px;
    top: 206px;
    width: 1120px;
    height: 788px;
    overflow: hidden;
  }
  .flyer__photo {
    position: absolute;
    inset: 0;
    background:
      linear-gradient(180deg, rgba(0,0,0,0) 92%, rgba(120,120,120,0.35) 96%, rgba(90,90,90,0.5) 100%),
      linear-gradient(90deg, var(--photo-light) 0%, var(--photo-mid) 45%, #cfcfcf 60%, #3a3a3a 70%, var(--photo-dark) 82%, #2a2a2a 94%, #e8e8e8 100%);
  }
  .brand {
    position: absolute;
    left: 71px;
    top: 70px;
    display: flex;
    align-items: center;
    gap: 22px;
  }
  .brand__mark {
    width: 38px;
    height: 38px;
    background: var(--brand-grey);
  }
  .brand__name {
    font-family: "Montserrat", sans-serif;
    font-weight: 300;
    font-size: 50px;
    letter-spacing: 2px;
    color: var(--brand-grey);
    line-height: 1;
  }
  .headline {
    position: absolute;
    left: 62px;
    top: 200px;
    width: 1000px;
    height: 170px;
  }
  .headline text {
    font-family: "Permanent Marker", cursive;
    font-size: 150px;
    fill: var(--gold);
  }
  .services {
    position: absolute;
    left: 69px;
    top: 450px;
    font-family: "Montserrat", sans-serif;
    font-weight: 400;
    font-size: 49px;
    letter-spacing: 0.5px;
    color: var(--gold);
    line-height: 1;
    white-space: nowrap;
  }
  .intro {
    position: absolute;
    left: 69px;
    top: 515px;
    font-family: "Figtree", sans-serif;
    font-size: 23px;
    line-height: 31.7px;
    color: var(--ink);
    white-space: nowrap;
  }
  .contact {
    position: absolute;
    left: 67px;
    top: 678px;
    font-family: "Montserrat", sans-serif;
    font-size: 16px;
    line-height: 26px;
    color: var(--gold);
    text-transform: uppercase;
    letter-spacing: 0.2px;
  }
</style>
</head>
<body>
  <main class="flyer">
    <div class="flyer__photo" role="img" aria-label="Black and white photograph of a person in a headstand yoga pose, silhouetted against a pale studio backdrop on the right side"></div>

    <div class="brand">
      <span class="brand__mark"></span>
      <span class="brand__name">MIRIAM BASKELL</span>
    </div>

    <svg class="headline" viewBox="0 0 1000 170" aria-label="Highstride">
      <text x="0" y="145" textLength="988" lengthAdjust="spacingAndGlyphs">HIGHSTRIDE</text>
    </svg>

    <h2 class="services">TRAINING, MENTORING</h2>

    <p class="intro">
      This is one of our highest in-demand programs and<br>
      is based on a background and proven track record<br>
      by Miriam in accelerating sales organisations and<br>
      their people into stand out high performers.
    </p>

    <p class="contact">
      www.miriambaskell.example<br>
      miriam@miriambaskell.example
    </p>
  </main>
</body>
</html>
```